KRV Ltd Business Card
Professional Biz Card for Kestrel Ridge Ventures IBC Ltd
KRV Ltd Business Card -
Creative Brief
Professional
Milo Harwick
President & CEO
milo@kestrelridgeventures.biz
www.kestrelridgeventures.biz
Skype ID: mharwick should be added.
www.kestrelridgeventures.biz & perhaps a large version of my logo.

```html
<!DOCTYPE html>
<html lang="en">
<head>
<meta charset="utf-8">
<title>KRV Ltd Business Card</title>
<link href="https://fonts.googleapis.com/css2?family=Arimo:wght@400;700&display=swap" rel="stylesheet">
<style>
  :root {
    --page: #f4f4f4;
    --card-top: #262626;
    --card-bottom: #050505;
    --ghost: #3a3a3a;
    --white: #ffffff;
    --soft: #d6d6d6;
    --silver-light: #f2f2f2;
    --silver-mid: #bdbdbd;
    --silver-dark: #8a8a8a;
    --ink: #1c1c1c;
  }
  * { margin: 0; padding: 0; box-sizing: border-box; }
  html, body {
    width: 1200px; height: 377px; overflow: hidden;
    background: var(--page);
    font-family: "Arimo", Arial, sans-serif;
  }
  .sheet { position: relative; width: 1200px; height: 377px; }
  .card {
    position: absolute; top: 12px; width: 576px; height: 355px;
    border-radius: 24px; overflow: hidden;
    background: linear-gradient(180deg, var(--card-top) 0%, var(--card-bottom) 55%, var(--card-bottom) 100%);
    box-shadow: 0 2px 6px rgba(0,0,0,0.25);
  }
  .card--front { left: 10px; }
  .card--back { left: 610px; }
  .ghost-name {
    position: absolute; left: 18px; top: -6px;
    font-weight: 700; font-size: 150px; letter-spacing: 14px;
    color: var(--ghost); line-height: 1;
  }
  .brand {
    position: absolute; left: 318px; top: 168px; width: 230px;
    display: flex; align-items: center; gap: 14px;
    color: var(--white); font-weight: 700; font-size: 78px; line-height: 1;
    letter-spacing: 4px;
  }
  .brand-mark { width: 22px; height: 22px; background: var(--white); flex: none; }
  .silver-bar {
    position: absolute; right: 0; height: 48px;
    background: linear-gradient(180deg, var(--silver-light) 0%, var(--silver-mid) 55%, var(--silver-dark) 100%);
  }
  .card--front .silver-bar { left: 230px; top: 276px; }
  .card--back .silver-bar { left: 314px; top: 283px; height: 42px; }
  .front-web {
    position: absolute; left: 266px; top: 290px;
    color: var(--ink); font-weight: 700; font-size: 17px;
  }
  .person { position: absolute; left: 26px; top: 150px; color: var(--white); }
  .person-name { font-size: 23px; font-weight: 400; }
  .person-title { font-size: 13px; color: var(--soft); margin-top: 3px; }
  .contact {
    position: absolute; left: 26px; top: 270px;
    color: var(--soft); font-size: 13px; line-height: 19px; list-style: none;
  }
</style>
</head>
<body>
<main class="sheet">
  <section class="card card--front" aria-label="Card front">
    <div class="ghost-name" aria-hidden="true">KRV</div>
    <div class="brand"><span class="brand-mark"></span>KRV</div>
    <div class="silver-bar"></div>
    <p class="front-web">www.kestrelridgeventures.biz</p>
  </section>

  <section class="card card--back" aria-label="Card back">
    <div class="ghost-name" aria-hidden="true">KRV</div>
    <div class="person">
      <p class="person-name">Milo Harwick</p>
      <p class="person-title">President &amp; CEO</p>
    </div>
    <div class="brand"><span class="brand-mark"></span>KRV</div>
    <ul class="contact">
      <li>Cell: +86 139 4270 5516</li>
      <li>Email: milo@kestrelridgeventures.biz</li>
      <li>www.kestrelridgeventures.biz</li>
    </ul>
    <div class="silver-bar"></div>
  </section>
</main>
</body>
</html>
```